OPF - Brochure 52 week Curriculum

Oak Path Fellows, Inc. wants to create a distribution Brochure. In the Bible (Matthew 28:18-20)- JESUS said to "TEACH" others what HE has commanded. we want to "PUT IN PRINT"

these 52 lines summarize HIS teachings
we want to use as our Curriculum teaching men ...

incorporate our statements and two main passages of scripture
(see attach pictures of headquarter lobby) to brand uniformity and consistency... we have summarized into 52 groups, but its NOT required to have numbers...
Purpose = obey GOD
Mission = love others
Vision = Development God fearing men globally.

The designer can have freedom in layout and sizing.
we were thinking bi fold , but again... designer has freedom
Please incorporate our colors (white, black, gray) using color wheel provided and our LOGO with website.

```html
<!DOCTYPE html>
<html lang="en">
<head>
<meta charset="utf-8">
<title>Oak Path Fellows – 52 Week Curriculum Brochure</title>
<link href="https://fonts.googleapis.com/css2?family=Poppins:wght@400;500;600;700;800&display=swap" rel="stylesheet">
<style>
  :root{
    --stage:#474747;
    --black:#000;
    --ink:#141414;
    --white:#fff;
    --panel-dark:#2b2b2b;
    --gray-band:#9a9a9a;
    --gray-head:#7d7d7d;
    --mist:#e6e5e8;
    --slate:#7a7a7a;
    --badge:#6e6e6e;
  }
  *{box-sizing:border-box;margin:0;padding:0}
  html,body{width:1200px;height:899px;overflow:hidden;background:var(--stage);font-family:'Poppins',sans-serif}
  .sheet{position:absolute;left:114px;width:971px;height:343px;display:flex}
  .sheet--outer{top:90px}
  .sheet--inner{top:466px}
  .panel{position:relative;width:50%;height:100%;overflow:hidden}

  /* cover panel */
  .cover{background:linear-gradient(180deg,#6b6b6b 0%,#3a3a3a 30%,#000 58%,#000 100%)}
  .cover__portrait{position:absolute;left:292px;top:0;width:194px;height:175px;
    background:radial-gradient(ellipse at 50% 40%,#8a8a8a 0%,#5c5c5c 45%,rgba(0,0,0,0) 80%)}
  .cover__kicker{position:absolute;left:25px;top:14px;font-weight:800;font-size:29px;letter-spacing:-.5px;color:#3c3c3c}
  .cover__title{position:absolute;left:23px;top:38px;font-weight:800;font-size:63px;letter-spacing:-1px;line-height:1;
    color:#d9d9d9;text-shadow:2px 3px 4px rgba(0,0,0,.6)}
  .cover__band{position:absolute;left:0;top:114px;width:259px;height:25px;background:var(--gray-band);
    clip-path:polygon(0 0,95% 0,100% 100%,0 100%);font-weight:700;font-size:11.2px;color:var(--ink);
    padding:5px 0 0 27px}

  .section{position:absolute;left:25px;right:25px}
  .section__title{font-weight:700;font-size:12px;line-height:1.15;margin-bottom:5px}
  .section__title--muted{color:var(--gray-head)}
  .section__title--light{color:var(--white)}
  .list{list-style:none}
  .item{display:grid;grid-template-columns:8px 1fr;column-gap:6px;font-size:6.2px;line-height:1.22;margin-bottom:6px}
  .list--tight .item{margin-bottom:3px}
  .item__num{width:8px;height:8px;border-radius:50%;background:var(--badge);color:var(--white);
    font-size:4.4px;font-weight:700;display:flex;align-items:center;justify-content:center;margin-top:-.5px}
  .on-dark{color:var(--white)}
  .on-dark .item__num{background:#cfcfcf;color:var(--ink)}
  .on-light{color:var(--ink)}
  .on-slate{color:var(--white)}
  .on-slate .item__num{background:#c4c4c4;color:var(--slate)}

  .ethics{background:radial-gradient(ellipse at 40% 10%,#4a4a4a 0%,#2d2d2d 55%,#262626 100%)}

  .inner-left .band{position:absolute;left:0;right:0}
  .band--white{background:var(--white)}
  .band--mist{background:var(--mist)}
  .band--slate{background:var(--slate)}
  .inner-right .band{position:absolute;left:0;right:0}
  .band--fade{background:linear-gradient(90deg,#dcdcdc 0%,#fff 18%)}

  .tag{position:absolute;left:344px;top:309px;width:142px;height:16px;background:var(--black);color:var(--white);
    font-weight:700;font-size:8.6px;clip-path:polygon(7% 0,100% 0,100% 100%,0 100%);padding:2px 0 0 16px;letter-spacing:.3px}
</style>
</head>
<body>

<!-- Outer spread -->
<section class="sheet sheet--outer">
  <div class="panel cover">
    <div class="cover__portrait" role="img" aria-label="Painted portrait of a bearded apostle with halo, in grayscale"></div>
    <div class="cover__kicker">JESUS SAID TO</div>
    <div class="cover__title">TEACH</div>
    <div class="cover__band">OTHERS WHAT HE HAS COMMANDED</div>

    <div class="section on-dark" style="top:177px">
      <h2 class="section__title section__title--muted">Regarding God and Righteousness</h2>
      <ol class="list">
        <li class="item"><span class="item__num">1</span><span>Repent: Change your mind and actions towards sin, as the Kingdom of Heaven is near.&nbsp; Turn away from sin and toward GOD. Matthew 4:17, Luke 13:3.&nbsp;&nbsp; Repent: This is the call to turn away from sin and embrace the good news of salvation through Jesus Christ. Found in Mark 1:15.</span></li>
        <li class="item"><span class="item__num">2</span><span>Accept the Good News of salvation offered through Jesus.</span></li>
        <li class="item"><span class="item__num">3</span><span>Believe in the Son of God, Jesus Christ: This is essential for salvation and receiving the Holy Spirit. John 6:29, John 14:11</span></li>
        <li class="item"><span class="item__num">4</span><span>Have faith in God, and trust in Jesus as the Son of God.</span></li>
        <li class="item"><span class="item__num">5</span><span>Be born again: John 3:7&nbsp; Be born again (of water and the Spirit): Experience a spiritual transformation necessary for entrance into God's Kingdom.</span></li>
        <li class="item"><span class="item__num">6</span><span>Give your utmost devotion and affection to God. Love God&nbsp; with all your heart, soul, mind, and strength: Matthew 22:37-38, Mark 12:30, Luke 10:27</span></li>
        <li class="item"><span class="item__num">7</span><span>Honor God's Law: Understand that Jesus did not come to abolish the Law but to fulfill it and to magnify its application in the heart.</span></li>
      </ol>
    </div>
  </div>

  <div class="panel ethics" role="img" aria-label="Faint grayscale church painting behind the text">
    <div class="section on-dark" style="top:18px">
      <h2 class="section__title section__title--light">Regarding Relationships and Ethics</h2>
      <ol class="list">
        <li class="item"><span class="item__num">8</span><span>Love your Neighbor as yourself: Matthew 22:39, Mark 12:31, Luke 10:27, Leviticus 19:18.&nbsp; Love one another, as I have loved you: Show sacrificial love to fellow believers.</span></li>
        <li class="item"><span class="item__num">9</span><span>The Golden Rule: Treat others as you would want to be treated. (Matthew 7:12).&nbsp; This encapsulates how to treat everyone with respect, kindness, and understanding.</span></li>
        <li class="item"><span class="item__num">10</span><span>Be reconciled to your brother: Seek peace and forgiveness when relationships are broken.</span></li>
        <li class="item"><span class="item__num">11</span><span>Go to those who offend you: Address offenses directly and privately before involving others.</span></li>
        <li class="item"><span class="item__num">12</span><span>Forgive offenders: Extend forgiveness to those who hurt you and forgive often. Forgive others: This is essential for receiving God's forgiveness.</span></li>
        <li class="item"><span class="item__num">13</span><span>Love your enemies and pray for those who persecute you: Matthew 5:44, Luke 6:27-28.&nbsp; Extend compassion even to those who mistreat you.</span></li>
      </ol>
      <h2 class="section__title section__title--light" style="margin-top:2px">Regarding Personal Conduct and Attitudes</h2>
      <ol class="list">
        <li class="item"><span class="item__num">14</span><span>Be baptized: Be immersed in water as a symbol of your new life in Christ.</span></li>
        <li class="item"><span class="item__num">15</span><span>Take, eat, and drink in remembrance of Me (Communion/Lord's Supper): Participate in the commemoration of Jesus' sacrifice.</span></li>
        <li class="item"><span class="item__num">16</span><span>Let your light shine before others: Matthew 5:16.&nbsp;&nbsp; Followers are called to live in such a way that their good deeds bring glory to GOD. Demonstrate good works to the world.</span></li>
        <li class="item"><span class="item__num">17</span><span>Care for the less fortunate: Help those in need, such as the hungry, thirsty, strangers, naked, sick, and imprisoned, according to Luke 14:13-14, Matthew 25:31-46.</span></li>
        <li class="item"><span class="item__num">18</span><span>Deny yourself, Take up your cross daily and follow Jesus: This signifies a commitment to discipleship, even in the face of hardship.&nbsp; this teaching is found in Luke 9:23-24; Matthew 16:24-25.&nbsp; Prioritize following Jesus above your own desires and be willing to endure hardship for His sake.</span></li>
        <li class="item"><span class="item__num">19</span><span>Fast: Engage in fasting, but do so for the right reasons and not for outward show.</span></li>
        <li class="item"><span class="item__num">20</span><span>Be wise as serpents and innocent as doves: Matthew 10:16</span></li>
        <li class="item"><span class="item__num">21</span><span>Do not worry about your life or material possessions: Trust God to provide for your needs. Trust God to provide for your needs. Matthew 6:34</span></li>
        <li class="item"><span class="item__num">22</span><span>Lay up treasures in heaven: Focus on building a spiritual inheritance rather than accumulating earthly wealth.&nbsp; Matthew 6:19-21</span></li>
        <li class="item"><span class="item__num">23</span><span>Be a servant: Seek greatness through humble service to others. Serve one another: Matthew 20:25-28</span></li>
      </ol>
    </div>
  </div>
</section>

<!-- Inner spread -->
<section class="sheet sheet--inner">
  <div class="panel inner-left">
    <div class="band band--white" style="top:0;height:114px"></div>
    <div class="band band--mist" style="top:114px;height:166px"></div>
    <div class="band band--white" style="top:280px;height:63px"></div>

    <div class="section on-light" style="top:20px">
      <h2 class="section__title section__title--muted">Prayer</h2>
      <ol class="list list--tight">
        <li class="item"><span class="item__num">24</span><span>Jesus provided guidance on prayer, teaching that it should be done in private and with sincerity (Matthew 6:5-8).</span></li>
        <li class="item"><span class="item__num">25</span><span>He also linked prayer to having a forgiving heart (Mark 11:25; Matthew 18:18-20). HE encouraged praying with simple faith and persistence (Luke 11:5-13; Matthew 21:21-22).</span></li>
        <li class="item"><span class="item__num">26</span><span>Pray: Engage in prayer consistently, with sincerity and according to Jesus' example.</span></li>
        <li class="item"><span class="item__num">27</span><span>Prayer for our enemies : Luke 23:24, Matthew 5:44</span></li>
        <li class="item"><span class="item__num">28</span><span>Pray for others : intercession</span></li>
        <li class="item"><span class="item__num">29</span><span>Pray for laborers: Seek God to send workers into the harvest field of souls. Pray for kingdom laborers: Matthew 9:38, Luke 10:2</span></li>
      </ol>
    </div>

    <div class="section on-light" style="top:122px;right:60px">
      <h2 class="section__title section__title--muted">Regarding Outreach and Discipleship</h2>
      <ol class="list">
        <li class="item"><span class="item__num">30</span><span>Go and make disciples of all nations: Evangelize and teach others to follow Jesus' commands: This is a central command, emphasizing the importance of evangelism and discipleship. Matthew 28:18-20. Teach others to obey all that Jesus commanded: Passing on the teachings of Christ to new believers is a key aspect of discipleship.</span></li>
        <li class="item"><span class="item__num">31</span><span>Feed My Sheep: Care for and nourish the spiritual lives of believers.</span></li>
        <li class="item"><span class="item__num">32</span><span>Receive God's power: Be filled with the Holy Spirit to effectively carry out God's work.</span></li>
      </ol>
    </div>

    <div class="section on-light" style="top:204px">
      <h2 class="section__title section__title--muted">Cautions and warnings</h2>
      <ol class="list">
        <li class="item"><span class="item__num">33</span><span>Beware of false prophets: Be discerning and recognize those who may mislead others with false teachings.</span></li>
        <li class="item"><span class="item__num">34</span><span>Beware of leaven (doctrine) of the Pharisees and Sadducees: Avoid hypocrisy and legalism.</span></li>
        <li class="item"><span class="item__num">35</span><span>Be alert and reliant on God's strength to overcome temptation.</span></li>
        <li class="item"><span class="item__num">36</span><span>Do not cast pearls before swine: Use discretion and avoid sharing sacred things with those who may devalue or disrespect them.</span></li>
      </ol>
    </div>

    <div class="section on-light" style="top:284px">
      <h2 class="section__title section__title--muted">Living as a Disciple</h2>
      <ol class="list">
        <li class="item"><span class="item__num">37</span><span>37.&nbsp; Be merciful: Show compassion to others, just as God is merciful.&nbsp; Act with kindness and compassion towards others.&nbsp; Luke 6:36</span></li>
        <li class="item"><span class="item__num">38</span><span>38.&nbsp; Care for those in distress: Help the hungry, thirsty, strangers, naked, sick, and imprisoned.</span></li>
      </ol>
    </div>
  </div>

  <div class="panel inner-right">
    <div class="band band--fade" style="top:0;height:114px"></div>
    <div class="band band--slate" style="top:114px;height:166px"></div>
    <div class="band band--fade" style="top:280px;height:63px"></div>

    <div class="section on-light" style="top:21px">
      <ol class="list">
        <li class="item"><span class="item__num">39</span><span>Recognize your own imperfections and avoid judging others harshly. Matthew 7:1-2, Luke 6:37.&nbsp; Focus on examining your own faults before criticizing others. He taught against judging others, stating that the standard by which you judge will be applied to you (Matthew 7:1-2).</span></li>
        <li class="item"><span class="item__num">40</span><span>Seek God's kingdom first: Make God and his righteousness your highest priority. Prioritize God's reign and right way of living above all else. Found in Matthew 6:33.</span></li>
        <li class="item"><span class="item__num">41</span><span>Abide in JESUS: John 15:4, John 6:35, 40, 47, John 14:27.</span></li>
        <li class="item"><span class="item__num">42</span><span>Follow JESUS: Matthew 4:19, Luke 5:28</span></li>
      </ol>
    </div>

    <div class="section on-slate" style="top:118px">
      <h2 class="section__title section__title--light" style="margin-bottom:3px">Forgiveness (Jesus Taught About The<br>Importance Of Both Receiving And Giving Forgiveness)</h2>
      <ol class="list">
        <li class="item" style="margin-bottom:5px"><span class="item__num">43</span><span>Forgive others: Matthew 6:12, 14, Mark 11:25-26, Luke 6:37</span></li>
        <li class="item" style="margin-bottom:5px"><span class="item__num">44</span><span>JESUS emphasized that forgiveness is linked to forgiving others (Matthew 6:14-15)</span></li>
        <li class="item" style="margin-bottom:5px"><span class="item__num">45</span><span>forgiveness should be extended limitlessly to those who repent (Luke 17:3-4; Matthew 18:21-22).</span></li>
        <li class="item" style="margin-bottom:5px"><span class="item__num">46</span><span>forgiveness is also illustrated as the cancellation of debt (Matthew 18:21-35).</span></li>
      </ol>
      <h2 class="section__title section__title--light" style="margin-bottom:3px">Humility and Service</h2>
      <ol class="list list--tight">
        <li class="item"><span class="item__num">47</span><span>JESUS stated that humility leads to being honored (Luke 14:11; Matthew 23:12)</span></li>
        <li class="item"><span class="item__num">48</span><span>True greatness is found in serving others (Matthew 20:26-28).</span></li>
        <li class="item"><span class="item__num">49</span><span>The Bible also states that God opposes the proud but shows favor to the humble (James 4:6; 1 Peter 5:5).</span></li>
      </ol>
      <h2 class="section__title section__title--light" style="margin:5px 0 3px">Warning Against Self-Righteousness and Judgment</h2>
      <ol class="list">
        <li class="item"><span class="item__num">50</span><span>Jesus warned against hypocrisy, particularly the hypocrisy of the Pharisees (Luke 12:1).</span></li>
      </ol>
    </div>

    <div class="section on-light" style="top:283px;right:10px">
      <h2 class="section__title section__title--muted" style="margin-bottom:4px">Money (Jesus Taught About Using Money and Possessions Responsibly.</h2>
      <ol class="list">
        <li class="item" style="margin-bottom:5px"><span class="item__num">51</span><span>JESUS advised storing up treasures in Heaven rather than on Earth (Matthew 6:19-21)</span></li>
        <li class="item"><span class="item__num">52</span><span>JESUS stated that it is impossible to serve both God and money (Matthew 6:24).</span></li>
      </ol>
    </div>

    <div class="tag">Matthew 28:18-20</div>
  </div>
</section>

</body>
</html>
```